Natural Skincare brand needs new labels!

We are a natural and organic skin care brand based in the united states. We are looking for unique product label designs that will help our brand stand out. We want the labels to look elegant and natural, but also incorporate some color. We want a design aspect like a line drawing on the labels, see examples. Please refer to our website to see our current labels and to get more of a feel of who we are. Our logo is included. We are looking for 5 labels for 5 different Products.
1. Body butter: 1.5"x9" rectangle wrap around 12oz jar with black lid
2. Eczema Salve: 1.5" circle silver metal tin
3. Glow Serum: 1.5"x3" rectangle Blue Dropper Bottle with black top
4. Mineral Mist: 1.5"x3" clear glass sprayer bottle (want clear label)
website: www.venalubotanics.com
Instagram: @venalubotanics

```html
<!DOCTYPE html>
<html lang="en">
<head>
<meta charset="utf-8">
<title>Venalu Skin – Body Butter Label</title>
<link href="https://fonts.googleapis.com/css2?family=Merriweather:wght@400&family=Open+Sans:wght@400;600&display=swap" rel="stylesheet">
<style>
  :root {
    --backdrop: #dcd9d7;
    --label-bg: #e5edbd;
    --sketch-tone: #c3cb9f;
    --sketch-deep: #aeb58d;
    --ink: #6a6a66;
    --ink-dark: #4d4d4a;
    --coral: #ee6e5e;
    --sun: #f4ee78;
  }
  * { margin: 0; padding: 0; box-sizing: border-box; }
  html, body {
    width: 1200px; height: 900px; overflow: hidden;
    background: var(--backdrop);
    font-family: "Open Sans", Arial, sans-serif;
  }
  .label {
    position: absolute; left: 30px; top: 358px;
    width: 1140px; height: 184px;
    background: var(--label-bg);
    overflow: hidden;
    box-shadow: 0 6px 14px rgba(0,0,0,0.18);
    color: var(--ink);
  }
  .sketch { position: absolute; }
  .sketch--leaf-corner {
    left: 0; top: 0; width: 170px; height: 120px;
    background: radial-gradient(ellipse at 30% 20%, var(--sketch-deep), var(--sketch-tone) 55%, transparent 75%);
    opacity: .55;
  }
  .sketch--fruit-branch {
    left: 370px; top: 0; width: 440px; height: 184px;
    background: radial-gradient(ellipse at 55% 65%, var(--sketch-deep) 0%, var(--sketch-tone) 45%, transparent 72%);
    opacity: .6;
  }
  .sun-band {
    position: absolute; left: 0; bottom: 0; width: 381px; height: 9px;
    background: linear-gradient(90deg, var(--sun), var(--sun) 40%, rgba(244,238,120,0));
  }
  .brand {
    position: absolute; left: 158px; top: 14px;
    display: flex; align-items: center; gap: 5px;
  }
  .brand__dot { width: 10px; height: 10px; border-radius: 50%; background: var(--coral); }
  .brand__name { font-size: 16px; font-weight: 600; color: var(--coral); letter-spacing: .5px; }
  .product {
    position: absolute; left: 90px; width: 220px; text-align: center;
  }
  .product__title {
    top: 70px; font-family: "Merriweather", Georgia, serif;
    font-size: 27px; color: var(--ink-dark);
  }
  .product__benefits { top: 110px; font-size: 11px; line-height: 14px; }
  .size { position: absolute; left: 181px; top: 148px; font-size: 13px; color: var(--ink-dark); }
  .scent { position: absolute; left: 255px; top: 146px; font-size: 15px; display: flex; align-items: center; gap: 3px; }
  .scent__pod { display: inline-block; width: 26px; height: 14px; border-radius: 50%; background: var(--sketch-deep); }
  .info { position: absolute; text-align: center; font-size: 9px; line-height: 11px; }
  .info__head { color: var(--coral); margin-bottom: 4px; }
  .ingredients { left: 877px; top: 14px; width: 140px; }
  .ingredients__organic { margin-top: 5px; font-weight: 600; color: var(--ink-dark); }
  .usage { left: 796px; top: 91px; width: 130px; }
  .follow { left: 1011px; top: 84px; width: 100px; }
  .follow__dot { width: 16px; height: 16px; border-radius: 50%; background: var(--coral); margin: 2px auto 4px; }
  .website { left: 867px; top: 154px; width: 160px; font-size: 10px; color: var(--ink-dark); }
</style>
</head>
<body>
  <section class="label">
    <div class="sketch sketch--leaf-corner" role="img" aria-label="Faint line drawing of leaves in the corner"></div>
    <div class="sketch sketch--fruit-branch" role="img" aria-label="Faint line drawing of a fruiting branch with leaves"></div>
    <div class="sun-band"></div>

    <div class="brand">
      <span class="brand__dot"></span>
      <span class="brand__name">Venalu Skin</span>
    </div>

    <h1 class="product product__title">Body Butter</h1>
    <p class="product product__benefits">Moulsturizing + Nourishing<br>Sensitive + Dry Skin</p>
    <p class="size">12 oz</p>
    <p class="scent">Cardamom <span class="scent__pod" role="img" aria-label="Small drawing of a cardamom pod"></span></p>

    <div class="info ingredients">
      <p class="info__head">Ingredients :</p>
      <p>shea butter*, mango butter*, kokum butter, coconut oil*, sesame oil*, vitamin E oil*, essential oils*, Cardamom</p>
      <p class="ingredients__organic">Organic</p>
    </div>
    <div class="info usage">
      <p class="info__head">How to use :</p>
      <p>Apply all over body as a daily moisturizer</p>
    </div>
    <div class="info follow">
      <p class="info__head">Follow us :</p>
      <div class="follow__dot"></div>
      <p>@venalubotanics</p>
    </div>
    <p class="info website">www.venalubotanics.com</p>
  </section>
</body>
</html>
```